Would like a design for lawn signs I will be using to advertise with. Attached are three images. One is the jpeg version of our logo to use in creating and editing the design. The other two are mock ups of our current style of tshirt and business card design. I would like the finished product to look similar in style to the mock ups. The actual color of our logo in the jpeg picture is outdated coloring. I would like the logo to be the color of the logo in the mock up tshirt version and the business card design.
The signs I will be using are white in color and 18"x24" white lawn signs, so I would like the logo to appear like the logo in the grey tshirt design, where it is black and orange. As for the text coloring I would like it to be black as well.
The only things I want included on the text of the sign design is:
Phone: 816-402-7761
Email: tidyturfco@fernmail.com
Mowing
Fertilization
Aeration
Bed & tree maintenance
and more.

```html
<!DOCTYPE html>
<html lang="en">
<head>
<meta charset="utf-8">
<title>Tidy Turf Lawn &amp; Landscape – Lawn Sign</title>
<link rel="stylesheet" href="https://fonts.googleapis.com/css2?family=Arimo:wght@700&display=swap">
<style>
  :root {
    --ink: #000000;
    --accent: #e8472f;
    --paper: #ffffff;
  }
  html, body {
    margin: 0;
    padding: 0;
    width: 900px;
    height: 1200px;
    overflow: hidden;
    background: var(--paper);
  }
  .sign {
    position: relative;
    width: 900px;
    height: 1200px;
    box-sizing: border-box;
    border: 9px solid var(--ink);
    background: var(--paper);
    font-family: "Arimo", Arial, sans-serif;
    font-weight: 700;
    color: var(--ink);
  }
  .brand-name {
    position: absolute;
    left: 0;
    top: 200px;
    width: 100%;
    margin: 0;
    text-align: center;
    font-weight: 700;
    color: var(--ink);
    line-height: 1;
  }
  .brand-name .brand-main {
    display: block;
    font-size: 128px;
    letter-spacing: 2px;
  }
  .brand-name .brand-sub {
    display: block;
    margin-top: 22px;
    font-size: 42px;
    letter-spacing: 4px;
  }
  .rules {
    position: absolute;
    left: 0;
    top: 0;
    width: 900px;
    height: 1200px;
    pointer-events: none;
  }
  .contact {
    position: absolute;
    left: 0;
    display: flex;
    align-items: center;
    font-size: 37px;
    line-height: 1;
  }
  .contact-phone { top: 665px; left: 158px; }
  .contact-email { top: 730px; left: 145px; }
  .contact svg { margin-right: 14px; flex: none; }
  .services {
    position: absolute;
    left: 143px;
    top: 838px;
    width: 614px;
    margin: 0;
    padding: 0;
    list-style: none;
    text-align: center;
    font-size: 38px;
    line-height: 52.5px;
  }
</style>
</head>
<body>
  <main class="sign">
    <h1 class="brand-name">
      <span class="brand-main">TIDY TURF</span>
      <span class="brand-sub">LAWN &amp; LANDSCAPE LLC</span>
    </h1>

    <svg class="rules" viewBox="0 0 900 1200" aria-hidden="true">
      <g fill="var(--ink)" stroke="var(--ink)" stroke-width="2">
        <line x1="100" y1="619" x2="799" y2="619"/>
        <circle cx="100" cy="619" r="8"/>
        <circle cx="799" cy="619" r="8"/>
        <polyline fill="none" points="143,1120 143,817 757,817 757,1120"/>
        <circle cx="143" cy="1120" r="8"/>
        <circle cx="757" cy="1120" r="8"/>
      </g>
    </svg>

    <div class="contact contact-phone">
      <svg width="28" height="36" viewBox="0 0 28 36" aria-label="Phone" role="img">
        <g fill="none" stroke="var(--accent)" stroke-width="2.6">
          <rect x="4" y="2" width="20" height="32" rx="3"/>
          <rect x="9" y="11" width="10" height="10"/>
          <line x1="9" y1="6" x2="19" y2="6"/>
        </g>
      </svg>
      <span>: 816-402-7761</span>
    </div>

    <div class="contact contact-email">
      <svg width="42" height="30" viewBox="0 0 42 30" aria-label="Email" role="img">
        <g fill="none" stroke="var(--accent)" stroke-width="2.6">
          <rect x="2" y="3" width="38" height="24"/>
          <polyline points="2,3 21,17 40,3"/>
          <line x1="2" y1="27" x2="16" y2="14"/>
          <line x1="40" y1="27" x2="26" y2="14"/>
        </g>
      </svg>
      <span>: tidyturfco@fernmail.com</span>
    </div>

    <ul class="services">
      <li>MOWING</li>
      <li>FERTILIZATION</li>
      <li>AERATION</li>
      <li>BED &amp; TREE MAINTENANCE</li>
      <li>AND MORE.</li>
    </ul>
  </main>
</body>
</html>
```